Business Card Design

we are a brand new cable TV network devoted to self improvement and leading a better life called FLOURISH TV.I have a logo. We have 3 executives that need cards.I want it to be a heavy stock card: professional but showing our creative nature

Industry/Entity Type

Business

Contact Information for Business Card

CLAUDIA SAENZ AMLIECEO350 San Juan DrPonte Vedra Beach FL 32082904-473-5953

```html
<!DOCTYPE html>
<html lang="en">
<head>
<meta charset="utf-8">
<title>FLOURISH TV – Business Cards</title>
<link rel="stylesheet" href="https://fonts.googleapis.com/css2?family=Archivo:wght@400;600;800&display=swap">
<style>
  :root {
    --stage: #2a2a2a;
    --card-dark: #1f1d1e;
    --card-light: #ffffff;
    --ink: #1c1c1c;
    --ink-soft: #2e2e2e;
    --accent: #c4202b;
    --on-dark: #f4f4f4;
  }
  * { box-sizing: border-box; margin: 0; padding: 0; }
  html, body {
    width: 1200px; height: 750px; overflow: hidden;
    background: var(--stage);
    font-family: "Archivo", Arial, sans-serif;
  }
  .stage {
    width: 1200px; height: 750px;
    display: flex; align-items: center; justify-content: center; gap: 60px;
  }
  .card {
    width: 525px; height: 300px;
    position: relative;
    box-shadow: 0 12px 30px rgba(0,0,0,.45);
  }
  .card--back {
    background: var(--card-dark);
    display: flex; align-items: center; justify-content: center;
  }
  .brand-name {
    font-weight: 800;
    letter-spacing: 0.5px;
    line-height: 1;
  }
  .card--back .brand-name { color: var(--on-dark); font-size: 54px; }
  .card--front { background: var(--card-light); }
  .card--front .brand-name {
    position: absolute; left: 40px; top: 62px;
    color: var(--ink); font-size: 44px;
  }
  .person { position: absolute; left: 42px; top: 140px; }
  .person__name {
    color: var(--accent); font-size: 17px; font-weight: 600; letter-spacing: 0.3px;
  }
  .person__role { color: var(--ink-soft); font-size: 15px; margin-top: 6px; }
  .contact {
    position: absolute; right: 40px; top: 150px;
    text-align: right; color: var(--ink-soft); font-size: 14px; line-height: 1.45;
  }
  .contact__phone { display: inline-flex; align-items: center; gap: 6px; }
  .contact__icon { width: 14px; height: 14px; fill: var(--accent); }
</style>
</head>
<body>
<main class="stage">
  <section class="card card--back">
    <span class="brand-name">FLOURISH TV</span>
  </section>
  <section class="card card--front">
    <span class="brand-name">FLOURISH TV</span>
    <div class="person">
      <p class="person__name">MARISOL DUVAL KERNO</p>
      <p class="person__role">CEO</p>
    </div>
    <address class="contact" style="font-style:normal">
      <p>718 Copper Hollow Ln</p>
      <p>Harrow Cove FL 30915</p>
      <p class="contact__phone">555-218-0476
        <svg class="contact__icon" viewBox="0 0 24 24" aria-hidden="true">
          <path d="M3 8c0-2 4-4 9-4s9 2 9 4v2h-5V8c-1-.6-2.5-1-4-1s-3 .4-4 1v2H3z"/>
          <path d="M6 12h12l2 8H4zm6 2a2.5 2.5 0 1 0 0 5 2.5 2.5 0 0 0 0-5z"/>
        </svg>
      </p>
    </address>
  </section>
</main>
</body>
</html>
```